Medical Centre Website

We need a new design for a medical centre based in Perth, Western Australia called 'Tarwick Valley Medical Centre'.

The medical centre does general practitioner work including general checkups, ecg, heart checks, woman's health and more servicing children and adults. They also do home visits on occasions where the patient cannot attend the centre.

They would like an information/brochure website where visitors can read up on the practice, send email and view their location.

The client wish the design to be clean, fresh and light. The main colours are a light purple/blue and to a dark navy blue. The client would not want the logo to be altered in any way. This includes changing the words colours or the image.

The final design should represent a loving, family friendly practice where patients can come to receive the best treatments.

We just need the end product to be presented to un in a layed psd format. The fonts must be as per the W3C standards.

**IMPORTANT**
I have received heaps of skype invites in the past. To treat everyone fairly, I do not add people to my skype list as in the past people expected us to give them the prize. If you have questions, please ask them in pixel forum as it may benefit others who are also designing the site. If I need to, I will send a message to the user.
Updates

Hi Designers,

Most designs we have received have been overly cluttered. Are you able to simplify the designs.

Cheers, Dorian

Hi Designers,

Some of the designs are quite attractive but aremore cluttered than I would like. If you have a look at the following design, the design is very simple and straight to the point. A lot of designs have too much wording and the reader can be put off. We are looking something more like:

fernoakclinic.com.au

I would prefer to see designs and have opened up the contest for a further 7 days.

Designers,

We have received feedback from the client and Quite frankly he don’t really like any of them.They are too cluttered and Americanised. All drab blue colours.
 
If you have a look at template monster, these designs are better and cleaner. We do not want heaps of writing on the front page.

If you look at the eariler examples such as kelbrookgp.com.au which I did myself, the client loves that simplicity of the site.

```html
<!DOCTYPE html>
<html lang="en">
<head>
<meta charset="utf-8">
<title>Tarwick Valley Medical Centre</title>
<link href="https://fonts.googleapis.com/css2?family=Lato:wght@400;700&family=Fredoka:wght@600&family=Oswald:wght@400&display=swap" rel="stylesheet">
<style>
  :root {
    --navy: #1560ae;
    --sky: #16b1f0;
    --sky-light: #7fd3f7;
    --nav-top: #4cb6ee;
    --nav-bottom: #0b86d1;
    --tab-top: #d9e6f7;
    --tab-bottom: #a9c3e6;
    --headline: #168fcf;
    --accent: #b24bc0;
    --accent-dark: #9a35a8;
    --accent-light: #d66ad8;
    --service-blue: #1a9ad6;
    --muted: #9a9a9a;
    --card-bg: #f6f6f6;
    --card-border: #e3e3e3;
    --text-dark: #2c3e55;
    --heart-red: #d8262a;
    --heart-soft: #f4b5b6;
  }
  * { box-sizing: border-box; margin: 0; padding: 0; }
  html, body { width: 1200px; height: 1103px; overflow: hidden; background: #fff; }
  body { position: relative; font-family: "Lato", Arial, sans-serif; color: var(--text-dark); }

  .top-tabs {
    position: absolute; left: 602px; top: 5px; width: 497px; height: 44px;
    background: linear-gradient(var(--tab-top), var(--tab-bottom));
    clip-path: polygon(0 0, 100% 0, 100% 100%, 22px 100%);
    display: flex; padding-left: 22px;
  }
  .top-tabs a {
    flex: 1; display: flex; align-items: center; justify-content: center;
    font-size: 14px; color: #24385a; text-decoration: none;
    border-left: 1px solid rgba(255,255,255,.55);
  }
  .top-tabs a:first-child { border-left: none; }

  .brand { position: absolute; left: 120px; top: 66px; color: var(--navy); font-weight: 400; }
  .brand-name { font-size: 43px; line-height: 46px; letter-spacing: .5px; }
  .brand-sub { font-size: 24px; letter-spacing: 4px; margin-left: 172px; margin-top: 2px; }

  .call-us {
    position: absolute; right: 101px; top: 63px; font-size: 16px; font-weight: 700;
    color: #7f8a99; display: flex; align-items: center; gap: 4px;
  }
  .call-us strong { color: var(--navy); }

  .search {
    position: absolute; left: 800px; top: 99px; width: 299px; height: 32px;
    background: #e9eff7; border: 1px solid #c9d5e6;
    display: flex; align-items: center; justify-content: space-between; padding: 0 10px 0 12px;
    font-size: 14px; color: #8b96a6;
  }

  .main-nav {
    position: absolute; left: 0; top: 196px; width: 1200px; height: 61px;
    background: linear-gradient(var(--nav-top), var(--nav-bottom));
    border-bottom: 2px solid #5ec2f3;
  }
  .main-nav ul { list-style: none; display: flex; position: absolute; left: 115px; height: 100%; }
  .main-nav li {
    display: flex; align-items: center; padding: 0 17px; font-size: 15px; color: #fff;
    border-left: 1px solid rgba(0,70,140,.35); box-shadow: inset 1px 0 rgba(255,255,255,.25);
  }
  .main-nav li:first-child { border-left: none; box-shadow: none; padding-left: 13px; }

  .hero-sky {
    position: absolute; left: 0; top: 259px; width: 1200px; height: 410px;
    background:
      linear-gradient(90deg, rgba(255,255,255,.35) 0%, rgba(255,255,255,0) 10%, rgba(255,255,255,0) 90%, rgba(255,255,255,.35) 100%),
      linear-gradient(var(--sky) 0%, var(--sky) 65%, var(--sky-light) 85%, #fff 100%);
  }
  .hero-card {
    position: absolute; left: 119px; top: 307px; width: 980px; height: 455px;
    background: #fff; border: 1px solid #dcdcdc; box-shadow: 0 2px 6px rgba(0,0,0,.12);
  }
  .hero-headline {
    position: absolute; left: 34px; top: 56px; white-space: nowrap;
    font-family: "Fredoka", "Arial Rounded MT Bold", sans-serif; font-weight: 600;
    font-size: 47px; line-height: 50px; color: var(--headline);
  }
  .hero-headline em { font-style: normal; color: var(--accent); }
  .read-story {
    position: absolute; left: 35px; top: 341px; width: 371px; height: 53px;
    background: linear-gradient(var(--accent-light), var(--accent-dark));
    border: 1px solid #8c2e99; color: #fff;
    font-family: "Fredoka", sans-serif; font-weight: 600; font-size: 25px;
    display: flex; align-items: center; justify-content: center; letter-spacing: .5px;
  }
  .hero-visual {
    position: absolute; left: 528px; top: 80px; width: 452px; height: 290px;
    background: radial-gradient(ellipse 60% 60% at 62% 48%, var(--heart-red) 0%, #e4585b 30%, var(--heart-soft) 55%, #fff 85%);
  }
  .slide-arrow {
    position: absolute; top: 511px; width: 48px; height: 48px; border-radius: 50%;
    background: var(--accent); display: flex; align-items: center; justify-content: center;
  }
  .slide-arrow.prev { left: 41px; }
  .slide-arrow.next { left: 1128px; }

  .slide-dots { position: absolute; left: 570px; top: 777px; display: flex; gap: 4px; }
  .slide-dots span { width: 16px; height: 16px; border-radius: 50%; background: #c8c8c8; border: 2px solid #e6e6e6; }
  .slide-dots span.active { background: #6d6d6d; }

  .services-title {
    position: absolute; left: 133px; top: 808px;
    font-family: "Oswald", "Arial Narrow", sans-serif; font-size: 22px; color: var(--service-blue);
  }
  .service-list { position: absolute; left: 133px; top: 845px; display: flex; gap: 7px; }
  .service-card {
    position: relative; width: 233px; height: 237px;
    background: var(--card-bg); border: 1px solid var(--card-border);
  }
  .service-photo {
    position: absolute; left: 10px; top: 12px; width: 211px; height: 111px;
    border: 4px solid #fff; box-shadow: 0 0 0 1px #ddd;
  }
  .service-card h3 {
    position: absolute; left: 13px; top: 135px; font-size: 14px; font-weight: 700; color: var(--service-blue);
  }
  .service-card p {
    position: absolute; left: 13px; top: 155px; width: 210px;
    font-size: 14px; line-height: 18px; color: var(--muted);
  }
  .service-rule { position: absolute; left: 10px; right: 10px; top: 224px; height: 2px; background: var(--accent); }
  .read-more {
    position: absolute; right: 10px; top: 200px; width: 86px; height: 26px; background: var(--accent);
    color: #fff; font-size: 12px; font-weight: 700; display: flex; align-items: center; justify-content: center;
  }
  .service-arrow {
    position: absolute; top: 944px; width: 38px; height: 38px; border-radius: 50%;
    background: #d7a0d9; border: 3px solid #e9c6ea; display: flex; align-items: center; justify-content: center;
  }
  .service-arrow.prev { left: 83px; }
  .service-arrow.next { left: 1100px; }
</style>
</head>
<body>

<nav class="top-tabs">
  <a>Appointment</a><a>Find A Doctor</a><a>Locations</a><a>Careers</a>
</nav>

<div class="brand">
  <div class="brand-name">Tarwick Valley</div>
  <div class="brand-sub">MEDICAL CENTRE</div>
</div>

<div class="call-us">
  <svg width="18" height="18" viewBox="0 0 24 24"><path fill="#1a9ad6" d="M6.6 10.8a15.1 15.1 0 0 0 6.6 6.6l2.2-2.2c.3-.3.7-.4 1-.2 1.1.4 2.3.6 3.6.6.6 0 1 .4 1 1V20c0 .6-.4 1-1 1A17 17 0 0 1 3 4c0-.6.4-1 1-1h3.5c.6 0 1 .4 1 1 0 1.3.2 2.5.6 3.6.1.3 0 .7-.2 1z"/></svg>
  Call US: <strong>888.5550.2671</strong>
</div>

<div class="search">
  <span>Search</span>
  <svg width="16" height="16" viewBox="0 0 16 16"><circle cx="9.5" cy="6.5" r="4.5" fill="none" stroke="#1560ae" stroke-width="2"/><line x1="6.3" y1="9.7" x2="1.5" y2="14.5" stroke="#1560ae" stroke-width="2.4" stroke-linecap="round"/></svg>
</div>

<nav class="main-nav">
  <ul>
    <li>HOME</li><li>SERVICES</li><li>LOCATION</li><li>MEET &nbsp;A DOCTOR</li><li>GET A CALL</li><li>CASE HISTORY</li><li>BLOG</li><li>TESTIMONIAL</li><li>CONTACT</li>
  </ul>
</nav>

<div class="hero-sky" role="img" aria-label="Bright blue sky with soft white clouds"></div>

<section class="hero-card">
  <h1 class="hero-headline">Did you take care<br>of <em>heart?</em><br>Don’t worry, we are<br>here to take care of<br>your <em>heart!</em></h1>
  <div class="read-story">READ THE FULL STORY</div>
  <div class="hero-visual" role="img" aria-label="Illustration of a red heart with a bandage across a heartbeat line"></div>
</section>

<div class="slide-arrow prev"><svg width="16" height="24" viewBox="0 0 16 24"><path d="M12 2 3 12l9 10" fill="none" stroke="#e6b8ea" stroke-width="2"/></svg></div>
<div class="slide-arrow next"><svg width="16" height="24" viewBox="0 0 16 24"><path d="M4 2l9 10-9 10" fill="none" stroke="#e6b8ea" stroke-width="2"/></svg></div>

<div class="slide-dots"><span></span><span class="active"></span><span></span><span></span></div>

<h2 class="services-title">OUR SERVICES</h2>

<div class="service-arrow prev"><svg width="12" height="14" viewBox="0 0 12 14"><path d="M10 1 2 7l8 6z" fill="#fff"/></svg></div>
<div class="service-arrow next"><svg width="12" height="14" viewBox="0 0 12 14"><path d="M2 1l8 6-8 6z" fill="#fff"/></svg></div>

<div class="service-list">
  <article class="service-card">
    <div class="service-photo" role="img" aria-label="Glowing blue heart scan with heartbeat trace" style="background:linear-gradient(135deg,#0d4f80,#3aa6d8 55%,#0a3a66)"></div>
    <h3>LOREM IPSUM DOLORS IT</h3>
    <p>Lorem ipsum dolor sit amet, consectetur adipiscing elit.</p>
    <div class="service-rule"></div><div class="read-more">READ MORE</div>
  </article>
  <article class="service-card">
    <div class="service-photo" role="img" aria-label="Doctor talking with a young girl patient" style="background:linear-gradient(90deg,#e8ddd4,#f4ece6 50%,#e6d2bf)"></div>
    <h3>LOREM IPSUM DOLORS IT</h3>
    <p>Lorem ipsum dolor sit amet, consectetur adipiscing elit.</p>
    <div class="service-rule"></div><div class="read-more">READ MORE</div>
  </article>
  <article class="service-card">
    <div class="service-photo" role="img" aria-label="Women relaxing together in a bright exercise room" style="background:linear-gradient(90deg,#d9d5cf,#efe9e2 50%,#cfc6bb)"></div>
    <h3>LOREM IPSUM DOLORS IT</h3>
    <p>Lorem ipsum dolor sit amet, consectetur adipiscing elit.</p>
    <div class="service-rule"></div><div class="read-more">READ MORE</div>
  </article>
  <article class="service-card">
    <div class="service-photo" role="img" aria-label="Doctor caring for a child resting in a hospital bed" style="background:linear-gradient(90deg,#e9e6e2,#f5f3f0 50%,#d9dde2)"></div>
    <h3>LOREM IPSUM DOLORS IT</h3>
    <p>Lorem ipsum dolor sit amet, consectetur adipiscing elit.</p>
    <div class="service-rule"></div><div class="read-more">READ MORE</div>
  </article>
</div>

</body>
</html>
```